Supplement label for Brain health

I need a design for a supplement this supplement is a brain boost supplement.

The Name is Cortiva Plus.

I have attached other labels I like. This is for 50 plus demographic so the lettering needs to be easy to read and stand out. I have attached a dummy label template that once the winner is choosen then they will get the real supplement facts etc.

Clean desgin easy to read.

This file must be finished in AI format.

Target Market(s)

50 plus 70 percent female 30 percent male

Industry/Entity Type

Supplement

Font styles to use
Other font styles liked:
• Myrid pro maybe

Requirements
Must have
• easy to read text so no colors that hide text or hard to read.

```html
<!DOCTYPE html>
<html lang="en">
<head>
<meta charset="utf-8">
<title>Cortiva Plus – Supplement Label</title>
<link href="https://fonts.googleapis.com/css2?family=PT+Sans+Narrow:wght@400;700&display=swap" rel="stylesheet">
<style>
  :root {
    --page: #f2f3f5;
    --band-dark: #0d2a35;
    --band-mid: #1d5a6c;
    --teal-deep: #0f2f3a;
    --silver-light: #eceaec;
    --silver-dark: #a8a4ab;
    --navy: #233a8c;
    --alert: #f4513a;
    --white: #ffffff;
    --text-soft: #e3e6ea;
    --capsule-text: #d0d4da;
  }
  * { margin: 0; padding: 0; box-sizing: border-box; }
  html, body { width: 834px; height: 1200px; overflow: hidden; background: var(--page); }
  .canvas { position: relative; width: 834px; height: 1200px; }
  .label {
    position: absolute; left: 0; top: 145px; width: 834px; height: 910px;
    overflow: hidden; background: var(--teal-deep);
  }
  .top-band {
    position: absolute; left: 0; top: 0; width: 100%; height: 99px;
    background: radial-gradient(ellipse at 50% 60%, var(--band-mid), var(--band-dark) 75%);
  }
  .name-band {
    position: absolute; left: 0; top: 105px; width: 100%; height: 200px;
    border-top: 6px solid var(--white); border-bottom: 6px solid var(--white);
    background: linear-gradient(90deg, var(--silver-dark) 0%, var(--silver-light) 10%, #cfcbd0 35%, var(--silver-light) 55%, #b7b2b9 85%, var(--silver-light) 100%);
  }
  .product-name {
    position: absolute; left: 112px; top: 22px;
    font-family: "PT Sans Narrow", sans-serif; font-weight: 700;
    font-size: 124px; line-height: 1; letter-spacing: 1px;
    color: var(--navy); white-space: nowrap;
  }
  .strength-badge {
    position: absolute; left: 102px; top: 272px; width: 430px; height: 99px;
    background: var(--alert); border: 7px solid var(--white); border-radius: 40px;
    font-family: "PT Sans Narrow", sans-serif; font-size: 46px; color: var(--white);
    display: flex; align-items: center; justify-content: center;
  }
  .body-area {
    position: absolute; left: 0; top: 311px; width: 100%; height: 599px;
    background:
      radial-gradient(ellipse 55% 40% at 70% 8%, rgba(63,178,208,0.85), transparent 70%),
      radial-gradient(ellipse 60% 50% at 30% 45%, rgba(60,120,140,0.6), transparent 75%),
      linear-gradient(180deg, #1b5566 0%, #24505d 50%, #3c4d55 100%);
  }
  .head-art {
    position: absolute; left: 269px; top: 461px; width: 340px; height: 449px;
  }
  .benefits {
    position: absolute; left: 121px; top: 520px;
    font-family: "PT Sans Narrow", sans-serif; font-size: 44px; line-height: 63px;
    color: var(--text-soft); list-style: none;
  }
  .count-box {
    position: absolute; left: 121px; top: 777px; width: 135px; height: 133px;
    background: var(--navy); display: flex; align-items: center; justify-content: center; gap: 4px;
  }
  .count-number {
    font-family: "PT Sans Narrow", sans-serif; font-weight: 700; font-size: 72px; color: var(--capsule-text);
  }
  .count-unit {
    font-family: "PT Sans Narrow", sans-serif; font-size: 15px; color: var(--capsule-text);
    writing-mode: vertical-rl; transform: rotate(180deg);
  }
</style>
</head>
<body>
<div class="canvas">
  <section class="label">
    <div class="top-band"></div>
    <div class="name-band">
      <h1 class="product-name">Cortiva Plus</h1>
    </div>
    <div class="body-area"></div>
    <div class="strength-badge">for maximum strength</div>
    <svg class="head-art" viewBox="0 0 340 449" role="img" aria-label="Illustration of a head silhouette in profile with a glowing blue brain">
      <defs>
        <radialGradient id="head-tone" cx="55%" cy="35%" r="70%">
          <stop offset="0%" stop-color="#2a6fa8"/>
          <stop offset="35%" stop-color="#0c1a26"/>
          <stop offset="100%" stop-color="#05080b" stop-opacity="0.9"/>
        </radialGradient>
      </defs>
      <rect width="340" height="449" rx="150" fill="url(#head-tone)"/>
    </svg>
    <ul class="benefits">
      <li>focus</li>
      <li>clarity</li>
      <li>and</li>
      <li>memory</li>
    </ul>
    <div class="count-box">
      <span class="count-number">60</span>
      <span class="count-unit">capsules</span>
    </div>
  </section>
</div>
</body>
</html>
```